Book cover required for new book business book (Otter Ambush SEO for Managed Service Providers)

We are finalizing publishing dates for our latest business book. The audience this book is targetting is IT business owners. Demographic age 30-50 years of age, male, middle class. The title of the book is Otter Ambush SEO for managed service providers. The author name is Dean Harrow. The book goes into details about how to improve SEO for IT businesses. The premise of the book is if a bear attacked a crowd of people, and you were in that crowd, you'd only have to be 1% faster to outrun the bear. The same is true for your IT Businesses website. You only have to put in 1% more effort into your SEO to be on page one of Zarvio.
We have been using a working draft image whilst the book has been in preproduction. I am unsure if this working image is licensed. Please find attached.

```html
<!DOCTYPE html>
<html lang="en">
<head>
<meta charset="utf-8">
<title>Otter Ambush SEO for Managed Service Providers — Book Cover</title>
<link rel="stylesheet" href="https://fonts.googleapis.com/css2?family=Open+Sans:wght@400;600;700;800&display=swap">
<style>
  :root {
    --page-bg: #dfe5e8;
    --cover-white: #ffffff;
    --navy: #15304a;
    --navy-soft: #1c3550;
    --seo-blue: #1f63b0;
    --title-deep: #163f4f;
    --title-mid: #2b6674;
    --title-light: #4f7f86;
    --photo-green: #7fa35a;
    --photo-green-dark: #5e8744;
    --photo-fur: #9a6a3c;
    --photo-water: #e9eff2;
  }
  * { margin: 0; padding: 0; box-sizing: border-box; }
  html, body {
    width: 1200px;
    height: 1200px;
    overflow: hidden;
    background: var(--page-bg);
    font-family: "Open Sans", Arial, sans-serif;
  }
  .book-cover {
    position: absolute;
    left: 230px;
    top: 45px;
    width: 740px;
    height: 1110px;
    background: var(--cover-white);
    overflow: hidden;
  }
  .cover-photo {
    position: absolute;
    left: 0;
    top: 0;
    width: 740px;
    height: 540px;
    background:
      radial-gradient(ellipse 42% 55% at 34% 48%, var(--photo-fur) 0%, rgba(154,106,60,0.85) 45%, rgba(154,106,60,0) 75%),
      radial-gradient(ellipse 22% 32% at 80% 60%, #d9bf95 0%, rgba(217,191,149,0.7) 50%, rgba(217,191,149,0) 80%),
      linear-gradient(180deg, var(--photo-green) 0%, var(--photo-green-dark) 55%, var(--photo-water) 92%);
  }
  .torn-edge {
    position: absolute;
    left: 0;
    top: 440px;
    width: 740px;
    height: 110px;
  }
  .cover-title {
    position: absolute;
    left: 0;
    width: 740px;
    text-align: center;
    line-height: 1;
    white-space: nowrap;
  }
  .title-main {
    top: 573px;
    font-size: 180px;
    font-weight: 800;
    letter-spacing: -0.01em;
    background: linear-gradient(160deg, var(--title-deep) 0%, var(--title-mid) 40%, var(--title-light) 60%, var(--title-deep) 100%);
    -webkit-background-clip: text;
    background-clip: text;
    color: transparent;
  }
  .title-sub {
    top: 765px;
    font-size: 84px;
    font-weight: 700;
    letter-spacing: -0.03em;
    color: var(--navy);
  }
  .title-sub .seo { color: var(--seo-blue); }
  .title-tagline {
    top: 869px;
    font-size: 30px;
    font-weight: 600;
    color: var(--navy-soft);
  }
  .title-tagline .lead { font-weight: 400; }
  .author-name {
    top: 972px;
    font-size: 64px;
    font-weight: 700;
    color: var(--navy);
  }
</style>
</head>
<body>
  <main class="book-cover">
    <div class="cover-photo" role="img" aria-label="Photograph of a brown bear splashing through a river with a salmon in its jaws, a lighter cub following, green blurred background"></div>
    <svg class="torn-edge" viewBox="0 0 740 110" preserveAspectRatio="none" aria-hidden="true">
      <path fill="#ffffff" d="M0 78 L30 70 L55 82 L90 74 L120 86 L160 80 L200 92 L240 84 L280 96 L320 88 L360 94 L400 86 L440 92 L480 80 L520 72 L560 66 L600 58 L640 54 L680 48 L710 44 L740 40 L740 110 L0 110 Z"/>
    </svg>
    <h1 class="cover-title title-main">OTTER</h1>
    <p class="cover-title title-sub">AMBUSH <span class="seo">SEO</span></p>
    <p class="cover-title title-tagline"><span class="lead">for</span> Managed Service Providers</p>
    <p class="cover-title author-name">DEAN HARROW</p>
  </main>
</body>
</html>
```